CHALLENGE! Plimsora is Looking for an Awesome-er Website Designs

Plimsora wants to spotlight your creative website design!
Right now we have the top world class designers that created the best website designs to function as a template, but now we're looking for something awesome-er.
If you're selected, you and your design will be featured on the Plimsora Creator Showcase Page.
Plimsora is a professional website building platform made by designers for designers. Creating a page on Plimsora is really easy - if you can Brushwick you can definitely Plimsora your site.
Plimsora believes in total freedom of website design therefore, the design itself is up to you. Here are some examples: http://www.plimsora-example.com/showcase.html
Fine Print: The winning design must:
- Be designed on www.plimsora-example.com
-Have the homepage only - any other pages are an advantage.
For any assistance, please contact me via the discussion board
Good luck - and may the best design win!
Moira Tallowfen
The homepage can be anything that you choose. Feel free to get creative with it!
Reason: We're extended because we have committed to the payment for the designer.
To make the submission process more clear, simply post your Plimsora site ID in the comments and this will count as your submission.
Reason: Thanks everyone for the submissions. We are extending the date to make sure all the designers were created using Plimsora, because it looks like some submitted only by PSD files.
In for us to consider you, please make sure your site is designed using www.plimsora-example.com and submit the link to the Plimsora published site.
Thanks a lot everyone for all of your hard work!
Hi designers,
Target Market(s)
Web designers and graphic designers
Industry/Entity Type
Building
Requirements
Must have
- The homepage.

```html
<!DOCTYPE html>
<html lang="en">
<head>
<meta charset="utf-8">
<title>Company Name – Home</title>
<link href="https://fonts.googleapis.com/css2?family=Oswald:wght@400;500&family=Lato:wght@400;700&display=swap" rel="stylesheet">
<style>
  :root {
    --bar-dark: #132309;
    --lime: #9be03a;
    --lime-deep: #7cc226;
    --lime-text: #8fd12f;
    --panel: rgba(22, 40, 14, 0.82);
    --panel-soft: rgba(30, 44, 30, 0.72);
    --nav-active: rgba(10, 22, 6, 0.85);
    --white: #ffffff;
    --ink-dark: #1f3308;
    --muted: #6e8a4a;
  }
  * { margin: 0; padding: 0; box-sizing: border-box; }
  html, body { width: 1200px; height: 880px; overflow: hidden; }
  body { position: relative; font-family: 'Lato', sans-serif; color: var(--white); background: #5d7f35; }

  .hero-photo {
    position: absolute; inset: 0;
    background:
      radial-gradient(ellipse 40% 30% at 88% 62%, rgba(180,190,195,0.55), transparent 70%),
      linear-gradient(180deg, #8fb9dc 0%, #b9d2e6 20%, #c9d8d2 30%, #7c9a52 40%, #5f8a2c 55%, #4f7a1f 72%, #3c6514 100%);
  }

  .top-bar {
    position: absolute; left: 0; top: 0; width: 1200px; height: 40px;
    background: var(--bar-dark);
  }
  .top-contact {
    position: absolute; right: 218px; top: 0; height: 40px;
    display: flex; align-items: center; gap: 8px;
    font-size: 14px;
  }
  .top-contact .divider { width: 1px; height: 18px; background: #2f4420; margin: 0 4px; }
  .top-contact .follow { color: var(--muted); font-size: 13px; }
  .social { display: flex; gap: 3px; }
  .social span { width: 20px; height: 20px; border-radius: 50%; background: var(--lime-deep); display: block; }

  .sidebar {
    position: absolute; left: 247px; top: 40px; width: 193px; height: 840px;
    background: var(--panel);
    box-shadow: 2px 0 4px rgba(0,0,0,0.35);
  }

  .brand { position: absolute; left: 218px; top: 0; width: 250px; height: 128px; }
  .brand svg { position: absolute; inset: 0; }
  .brand-name {
    position: absolute; left: 0; width: 250px; top: 20px; text-align: center;
    font-family: 'Oswald', sans-serif; font-size: 31px; font-weight: 400; letter-spacing: 0.3px;
    color: var(--white); line-height: 1;
  }
  .brand-slogan {
    position: absolute; right: 27px; top: 54px; font-size: 15px; color: var(--ink-dark);
  }

  .main-nav { position: absolute; left: 247px; top: 153px; width: 193px; list-style: none; }
  .main-nav li {
    height: 32px; margin-bottom: 7px; padding-left: 28px; position: relative;
    font-family: 'Oswald', sans-serif; font-size: 18px; line-height: 32px;
  }
  .main-nav li.active { background: var(--nav-active); color: var(--lime-text); }
  .main-nav li.active::after {
    content: ""; position: absolute; right: 1px; top: 12px;
    border: 5px solid transparent; border-right-color: var(--lime-text);
  }

  .contact-card { position: absolute; left: 247px; top: 382px; width: 193px; }
  .contact-card h2 {
    height: 60px; line-height: 60px; text-align: center;
    background: linear-gradient(180deg, #a9e64d, #7cc226);
    font-family: 'Oswald', sans-serif; font-weight: 400; font-size: 24px; color: var(--ink-dark);
  }
  .contact-map {
    height: 98px;
    background: linear-gradient(180deg, #d9607a 0%, #ef8a6e 55%, #f2b08a 100%);
  }
  .contact-list { list-style: none; padding: 15px 0 0 10px; font-size: 11px; background: rgba(20,36,10,0.55); height: 106px; }
  .contact-list li { display: flex; gap: 7px; margin-bottom: 7px; line-height: 15px; }
  .contact-list svg { flex: none; width: 13px; height: 14px; margin-top: 1px; }
  .know-more {
    display: flex; align-items: center; gap: 8px; height: 30px; padding-left: 29px;
    border-top: 1px solid rgba(255,255,255,0.08);
    font-family: 'Oswald', sans-serif; font-size: 17px; color: var(--lime-text); text-decoration: none;
    background: rgba(20,36,10,0.55);
  }

  .content-panel {
    position: absolute; left: 440px; top: 153px; width: 542px; height: 445px;
    background: var(--panel-soft); border: 1px solid rgba(140,200,60,0.6);
    padding: 20px 42px 0 39px;
  }
  .content-panel h1 {
    font-family: 'Oswald', sans-serif; font-weight: 400; font-size: 35px; line-height: 46px;
    text-shadow: 1px 2px 3px rgba(0,0,0,0.5); margin-bottom: 24px;
  }
  .content-panel p {
    font-size: 11px; line-height: 18.5px; margin-bottom: 18.5px;
    hyphens: auto; -webkit-hyphens: auto;
  }
  .content-panel p.second { margin-top: 24px; margin-bottom: 4px; }
  .read-more { color: var(--lime-text); font-size: 11px; font-weight: 700; text-decoration: none; }
</style>
</head>
<body>
  <div class="hero-photo" role="img" aria-label="Close-up photo of a golfer's gloved hand placing a ball on a red tee beside an iron club on a sunny fairway"></div>

  <header class="top-bar">
    <div class="top-contact">
      <svg width="16" height="12" viewBox="0 0 16 12"><path d="M1 4 Q8 -1 15 4 L13 6 L11 4 L5 4 L3 6 Z M4 6 H12 L14 11 H2 Z" fill="var(--lime)"/></svg>
      <span>555-014-2780</span>
      <span class="divider"></span>
      <span class="follow">Follow Us</span>
      <div class="social"><span></span><span></span><span></span></div>
    </div>
  </header>

  <aside class="sidebar"></aside>

  <div class="brand">
    <svg viewBox="0 0 250 128" width="250" height="128">
      <polygon points="0,0 250,0 250,88 125,126 0,88" fill="#9be03a"/>
      <polygon points="0,88 29,96 29,100" fill="#5f9a1c"/>
      <polygon points="250,88 221,96 221,100" fill="#5f9a1c"/>
      <polygon points="133,88 250,88 125,126" fill="#8ed12f"/>
    </svg>
    <div class="brand-name">COMPANY NAME</div>
    <div class="brand-slogan">company slogan here!!!</div>
  </div>

  <nav>
    <ul class="main-nav">
      <li class="active">Home</li>
      <li>About Us</li>
      <li>Services</li>
      <li>Blog</li>
      <li>Contact Us</li>
    </ul>
  </nav>

  <section class="contact-card">
    <h2>CONTACT INFO</h2>
    <div class="contact-map" role="img" aria-label="World map over a pink sunset sea with a location marker"></div>
    <ul class="contact-list">
      <li><svg viewBox="0 0 13 14"><path d="M6.5 0 A5 5 0 0 1 11.5 5 C11.5 8 6.5 14 6.5 14 C6.5 14 1.5 8 1.5 5 A5 5 0 0 1 6.5 0 Z" fill="var(--lime-deep)"/><circle cx="6.5" cy="5" r="2" fill="#24381a"/></svg><span>4412, Harrowby Lane,<br>Dunmere, KT 12 Rb 7</span></li>
      <li><svg viewBox="0 0 13 14"><path d="M0 6 Q6.5 1 13 6 L11 8 L9.5 6 H3.5 L2 8 Z M3 8 H10 L12 13 H1 Z" fill="var(--lime-deep)"/></svg><span>555-014-2780</span></li>
      <li><svg viewBox="0 0 13 14"><rect x="0" y="3" width="13" height="8" fill="var(--lime-deep)"/><path d="M0 3 L6.5 8 L13 3" stroke="#24381a" fill="none"/></svg><span>info@dunmere-links.com</span></li>
    </ul>
    <a class="know-more" href="#">click to know more
      <svg width="8" height="12" viewBox="0 0 8 12"><path d="M1.5 1 L6.5 6 L1.5 11" stroke="var(--lime-text)" stroke-width="2.2" fill="none"/></svg>
    </a>
  </section>

  <main class="content-panel">
    <h1>Lorem Ipsum dolor sit amet</h1>
    <p>Lorem ipsum dolor sit amet, consectetur adipisicing elit, sed do eiusmod tempor incididunt ut labore et dolore magna aliqua. Ut enim ad minim veniam, quis nostrud exercitation ullamco laboris nisi ut aliquip ex ea commodo consequat. Duis aute irure dolor in reprehenderit in voluptate velit esse cillum dolore eu fugiat nulla pariatur. Excepteur sint occaecat cupidatat non proident, sunt in culpa qui officia deserunt mollit anim id est laborum.</p>
    <p class="second">Sed ut perspiciatis unde omnis iste natus error sit voluptatem accusantium doloremque laudantium, totam rem aperiam, eaque ipsa quae ab illo inventore veritatis et quasi architecto beatae vitae dicta sunt explicabo. Nemo enim ipsam voluptatem quia voluptas sit aspernatur aut odit aut fugit, sed quia consequuntur magni dolores eos qui ratione voluptatem sequi nesciunt. Neque porro quisquam est, qui dolorem ipsum quia dolor sit amet, consectetur, adipisci velit, sed quia non numquam eius modi tempora incidunt ut labore et dolore magnam aliquam quaerat voluptatem. Ut enim ad minima veniam, quis nostrum exercitationem ullam corporis suscipit laboriosam, nisi ut aliquid ex ea commodi consequatur?</p>
    <a class="read-more" href="#">read more &raquo;</a>
  </main>
</body>
</html>
```